Coffeeshop menu for filter tip

We want to have a cannabis (coffeeshop) menu in the size 25mm wide x 60mm wide. Some examples attached.

it must have the following text:
Menu

WEED p/g
Velotrine €16
Cinderfox €14
Tide Rambler €14
Marigolden €16
Grand Pelican €14
Copper Comet €14

HASH p/g
Baltic Ember €12
Harbor Velvet€11
Plum Rova €14
Dusk Maple €10

Target Market(s)

tourist in Amsterdam

Requirements
Nice to have
• cannabis sign leaf
• No Cigarettes allowed symbol

```html
<!DOCTYPE html>
<html lang="en">
<head>
<meta charset="utf-8">
<title>Coffeeshop Menu</title>
<link href="https://fonts.googleapis.com/css2?family=Dosis:wght@500;600&family=Michroma&family=Montserrat:wght@600;700&display=swap" rel="stylesheet">
<style>
  :root {
    --frame-green: #22c322;
    --leaf-green: #2fd22f;
    --text-green: #2ed12e;
    --price-white: #ffffff;
    --label-grey: #a9a9a9;
    --title-grey: #cfcfcf;
    --bg-top: #141c14;
    --bg-bottom: #1f6a1f;
    --box-bg: rgba(6, 10, 6, 0.82);
    --sign-red: #e0201e;
    --sign-dark: #141414;
  }
  * { margin: 0; padding: 0; box-sizing: border-box; }
  html, body { width: 1200px; height: 2880px; overflow: hidden; }
  body { background: var(--frame-green); position: relative; }

  .menu-board {
    position: absolute; left: 35px; top: 35px; width: 1130px; height: 2810px;
    background: linear-gradient(180deg, var(--bg-top) 0%, #17301a 40%, #1c4e1d 75%, var(--bg-bottom) 100%);
    overflow: hidden;
  }
  .leaf-art { position: absolute; border-radius: 50%; }
  .leaf-art--top { left: 620px; top: -40px; width: 620px; height: 720px;
    background: radial-gradient(ellipse at center, rgba(47,210,47,0.28) 0%, rgba(47,210,47,0.08) 55%, rgba(47,210,47,0) 72%); }
  .leaf-art--left { left: -160px; top: 420px; width: 560px; height: 620px;
    background: radial-gradient(ellipse at center, rgba(47,210,47,0.22) 0%, rgba(47,210,47,0.06) 55%, rgba(47,210,47,0) 72%); }
  .leaf-art--middle { left: 320px; top: 1180px; width: 900px; height: 900px;
    background: radial-gradient(ellipse at center, rgba(0,0,0,0.22) 0%, rgba(0,0,0,0.08) 55%, rgba(0,0,0,0) 72%); }
  .leaf-art--bottom { left: -200px; top: 2150px; width: 820px; height: 820px;
    background: radial-gradient(ellipse at center, rgba(47,210,47,0.45) 0%, rgba(47,210,47,0.15) 50%, rgba(47,210,47,0) 72%); }

  .menu-title {
    position: absolute; left: 62px; top: 70px;
    font-family: "Montserrat", sans-serif; font-weight: 600;
    font-size: 180px; line-height: 1; letter-spacing: 4px;
    color: var(--title-grey);
  }

  .price-section {
    position: absolute; left: 109px; width: 912px;
    border: 3px solid var(--frame-green);
    background: var(--box-bg);
  }
  .price-section--weed { top: 427px; height: 1087px; }
  .price-section--hash { top: 1688px; height: 784px; }

  .section-tab {
    position: absolute; left: -3px; top: -3px; width: 330px; height: 95px;
    background: var(--frame-green);
    font-family: "Michroma", sans-serif; font-size: 58px; line-height: 95px;
    color: #000; padding-left: 34px; letter-spacing: 2px;
  }
  .unit-label {
    position: absolute; right: 53px; top: 48px;
    font-family: "Dosis", sans-serif; font-weight: 500; font-size: 64px;
    color: var(--label-grey);
  }

  .price-row {
    position: absolute; left: 61px; right: 53px; height: 100px;
    display: flex; align-items: baseline;
    font-family: "Dosis", sans-serif; font-weight: 600; font-size: 80px; line-height: 100px;
  }
  .item-name { color: var(--text-green); white-space: nowrap; }
  .leader {
    flex: 1; margin: 0 30px 0 22px; height: 0;
    border-bottom: 2px solid var(--frame-green); opacity: 0.75;
    align-self: center; transform: translateY(20px);
  }
  .item-price { color: var(--price-white); min-width: 120px; text-align: right; }

  .no-cigarettes {
    position: absolute; left: 813px; top: 2554px; width: 250px; height: 192px;
    border: 3px solid var(--sign-red); border-radius: 10px;
    background: var(--sign-dark);
  }
  .no-cigarettes svg { display: block; }
</style>
</head>
<body>
  <main class="menu-board">
    <div class="leaf-art leaf-art--top" role="img" aria-label="Large cannabis leaf illustration"></div>
    <div class="leaf-art leaf-art--left" role="img" aria-label="Cannabis leaf illustration"></div>
    <div class="leaf-art leaf-art--middle" role="img" aria-label="Faint cannabis leaf silhouette"></div>
    <div class="leaf-art leaf-art--bottom" role="img" aria-label="Bright cannabis leaf illustration"></div>

    <h1 class="menu-title">MENU</h1>

    <section class="price-section price-section--weed">
      <h2 class="section-tab">WEED</h2>
      <span class="unit-label">P/G</span>
      <div class="price-row" style="top:176px"><span class="item-name">VELOTRINE</span><span class="leader"></span><span class="item-price">€16</span></div>
      <div class="price-row" style="top:325px"><span class="item-name">CINDERFOX</span><span class="leader"></span><span class="item-price">€14</span></div>
      <div class="price-row" style="top:474px"><span class="item-name">TIDE RAMBLER</span><span class="leader"></span><span class="item-price">€14</span></div>
      <div class="price-row" style="top:624px"><span class="item-name">MARIGOLDEN</span><span class="leader"></span><span class="item-price">€16</span></div>
      <div class="price-row" style="top:773px"><span class="item-name">GRAND PELICAN</span><span class="leader"></span><span class="item-price">€14</span></div>
      <div class="price-row" style="top:923px"><span class="item-name">COPPER COMET</span><span class="leader"></span><span class="item-price">€14</span></div>
    </section>

    <section class="price-section price-section--hash">
      <h2 class="section-tab">HASH</h2>
      <span class="unit-label">P/G</span>
      <div class="price-row" style="top:176px"><span class="item-name">BALTIC EMBER</span><span class="leader"></span><span class="item-price">€12</span></div>
      <div class="price-row" style="top:323px"><span class="item-name">HARBOR VELVET</span><span class="leader"></span><span class="item-price">€11</span></div>
      <div class="price-row" style="top:473px"><span class="item-name">PLUM ROVA</span><span class="leader"></span><span class="item-price">€14</span></div>
      <div class="price-row" style="top:622px"><span class="item-name">DUSK MAPLE</span><span class="leader"></span><span class="item-price">€10</span></div>
    </section>

    <div class="no-cigarettes">
      <svg width="244" height="186" viewBox="0 0 244 186" role="img" aria-label="No cigarettes sign">
        <text x="18" y="122" font-family="Montserrat, sans-serif" font-weight="700" font-size="118" fill="#000" stroke="#000">N</text>
        <circle cx="175" cy="82" r="46" fill="none" stroke="var(--sign-red)" stroke-width="11"/>
        <rect x="138" y="76" width="62" height="14" fill="#000"/>
        <line x1="143" y1="50" x2="207" y2="114" stroke="var(--sign-red)" stroke-width="11"/>
        <text x="122" y="170" text-anchor="middle" font-family="Montserrat, sans-serif" font-weight="700" font-size="29" fill="var(--sign-red)">CIGARETTES</text>
      </svg>
    </div>
  </main>
</body>
</html>
```